" Produz cachaça artesanal, no interior de Minas Gerais na cidade de Conceição do Mato Dentro Estrada Real, em alambiques de cobre. Produto feito a mao. "

```html
<!DOCTYPE html>
<html lang="pt-BR">
<head>
<meta charset="UTF-8">
<title>Lauro Cachaça Branca – Rótulo</title>
<link rel="stylesheet" href="https://fonts.googleapis.com/css2?family=Cormorant+Garamond:wght@500;600;700&family=Cormorant+SC:wght@500;600&family=Italianno&display=swap">
<style>
  :root {
    --parchment-light: #fbf1d3;
    --parchment-mid: #f0d9a0;
    --parchment-deep: #d9b070;
    --panel-light: #f3e0ad;
    --panel-mid: #ddb878;
    --panel-deep: #b9894a;
    --panel-shadow: #9c6f38;
    --silver-light: #f6f7f8;
    --silver-mid: #b4b8bd;
    --silver-dark: #5f6369;
    --band-black: #0e0e0e;
    --band-white: #fbfbf8;
    --band-brown: #2a2017;
    --ink: #1a1713;
    --name-silver: #7d8288;
  }
  * { margin: 0; padding: 0; box-sizing: border-box; }
  html, body { width: 1200px; height: 1200px; overflow: hidden; }
  body { position: relative; background: var(--parchment-light); }

  .route-map-backdrop {
    position: absolute; inset: 0;
    background:
      radial-gradient(ellipse 40% 30% at 18% 30%, rgba(201,160,95,0.35), transparent 70%),
      radial-gradient(ellipse 35% 30% at 85% 70%, rgba(201,160,95,0.35), transparent 70%),
      radial-gradient(ellipse at 50% 50%, var(--parchment-light) 0%, var(--parchment-mid) 65%, var(--parchment-deep) 100%);
  }

  .label-shape { position: absolute; inset: 0; width: 1200px; height: 1200px; }

  .label-text { position: absolute; left: 0; width: 1200px; text-align: center; }

  .brand-name {
    top: 262px;
    font-family: "Cormorant Garamond", serif;
    font-weight: 700;
    font-size: 200px;
    line-height: 200px;
    color: var(--name-silver);
    letter-spacing: 1px;
  }
  .brand-name .brand-dot {
    display: inline-block; width: 30px; height: 30px; border-radius: 50%;
    background: var(--name-silver); margin-left: 16px; vertical-align: 26px;
  }

  .product-type {
    top: 573px;
    font-family: "Italianno", cursive;
    font-size: 56px;
    line-height: 48px;
    color: var(--band-white);
  }
  .origin-town {
    top: 630px;
    font-family: "Cormorant SC", serif;
    font-weight: 600;
    font-size: 34px;
    line-height: 46px;
    color: var(--ink);
    letter-spacing: 1px;
  }
  .alcohol-content {
    top: 969px;
    font-family: "Cormorant Garamond", serif;
    font-weight: 600;
    font-size: 22px;
    line-height: 30px;
    color: var(--parchment-mid);
    letter-spacing: 2px;
  }
  .volume {
    top: 1030px;
    font-family: "Cormorant Garamond", serif;
    font-weight: 700;
    font-size: 46px;
    line-height: 52px;
    color: var(--ink);
    letter-spacing: 1px;
  }
</style>
</head>
<body>
  <div class="route-map-backdrop" role="img" aria-label="Antigo mapa da Estrada Real em tons de pergaminho ao fundo"></div>

  <svg class="label-shape" viewBox="0 0 1200 1200" xmlns="http://www.w3.org/2000/svg">
    <defs>
      <linearGradient id="silverFrame" x1="0" y1="0" x2="1" y2="0">
        <stop offset="0" stop-color="#5f6369"/>
        <stop offset="0.08" stop-color="#f6f7f8"/>
        <stop offset="0.3" stop-color="#9ea2a8"/>
        <stop offset="0.55" stop-color="#e9eaec"/>
        <stop offset="0.8" stop-color="#8f9399"/>
        <stop offset="0.93" stop-color="#f6f7f8"/>
        <stop offset="1" stop-color="#5f6369"/>
      </linearGradient>
      <radialGradient id="panelFill" cx="0.5" cy="0.42" r="0.75">
        <stop offset="0" stop-color="#f3e0ad"/>
        <stop offset="0.45" stop-color="#ddb878"/>
        <stop offset="0.8" stop-color="#b9894a"/>
        <stop offset="1" stop-color="#9c6f38"/>
      </radialGradient>
      <radialGradient id="panelTone" cx="0.65" cy="0.3" r="0.35">
        <stop offset="0" stop-color="#a9783e" stop-opacity="0.45"/>
        <stop offset="1" stop-color="#a9783e" stop-opacity="0"/>
      </radialGradient>
      <linearGradient id="footFill" x1="0" y1="0" x2="0" y2="1">
        <stop offset="0" stop-color="#ffffff"/>
        <stop offset="1" stop-color="#c4c7cc"/>
      </linearGradient>
    </defs>

    <path class="label-frame" fill="url(#silverFrame)" stroke="#4f5358" stroke-width="2"
      d="M276 190 Q276 60 420 50 Q600 30 780 50 Q924 60 924 190 L924 930 L820 1124 Q600 1140 380 1124 L276 930 Z"/>

    <g role="img" aria-label="Mapa antigo da Estrada Real no painel do rótulo">
      <path class="label-panel" fill="url(#panelFill)"
        d="M304 195 Q304 86 430 77 Q600 60 770 77 Q896 86 896 195 L896 925 L805 1097 Q600 1110 395 1097 L304 925 Z"/>
      <path class="label-panel-tone" fill="url(#panelTone)"
        d="M304 195 Q304 86 430 77 Q600 60 770 77 Q896 86 896 195 L896 925 L805 1097 Q600 1110 395 1097 L304 925 Z"/>
    </g>

    <rect class="type-band" x="377" y="574" width="446" height="44" fill="var(--band-black)"/>
    <rect class="origin-band" x="365" y="628" width="470" height="50" fill="var(--band-white)" stroke="var(--silver-mid)" stroke-width="2"/>

    <line x1="326" y1="962" x2="874" y2="962" stroke="url(#silverFrame)" stroke-width="5"/>
    <rect class="alcohol-band" x="330" y="965" width="540" height="36" fill="var(--band-brown)"/>
    <line x1="334" y1="1004" x2="866" y2="1004" stroke="url(#silverFrame)" stroke-width="5"/>

    <path class="label-foot" fill="url(#footFill)"
      d="M351 1008 L849 1008 L805 1097 Q600 1110 395 1097 Z"/>
  </svg>

  <div class="label-text brand-name">Lauro<span class="brand-dot"></span></div>
  <div class="label-text product-type">Cachaça Branca</div>
  <div class="label-text origin-town">Conceição do Mato Dentro</div>
  <div class="label-text alcohol-content">42% ALC/VOL.</div>
  <div class="label-text volume">750ML</div>
</body>
</html>
```